Pop-up Banner

Would like a design for a pop-up 85 x 206cm banner for a trade show. (from norla press)
We would like "our logo" (brightwave holdings) - then the tagline - "Your Trusted Partner in Data-Driven Decisions"
*Supporting Bullets*
Unified data, analytics & AI
Trusted insights, faster outcomes
Real-time intelligence at scale
Enterprise-ready, secure solutions
Clarity from data complexity
trusted by...some company logos
Partners with : partner logo
Our Colours: #FFA300, #3D4176, #FDD16E, #F87C57, #A68118, #1C2F36

```html
<!DOCTYPE html>
<html lang="en">
<head>
<meta charset="utf-8">
<title>Brightwave Holdings – Pop-up Banner</title>
<link rel="stylesheet" href="https://fonts.googleapis.com/css2?family=Open+Sans:wght@400;600;700&display=swap">
<style>
  :root {
    --orange: #FFA300;
    --navy: #3D4176;
    --ink: #1C2F36;
    --text: #111111;
    --white: #FFFFFF;
    --stage: #E4E4E4;
  }
  html, body {
    margin: 0;
    width: 1200px;
    height: 1200px;
    overflow: hidden;
    background: var(--stage);
    font-family: "Open Sans", Arial, sans-serif;
  }
  .banner {
    position: absolute;
    left: 380px;
    top: 67px;
    width: 440px;
    height: 1066px;
    background: var(--white);
    overflow: hidden;
  }
  .banner-shapes {
    position: absolute;
    left: 0;
    top: 0;
  }
  .brand {
    position: absolute;
    left: 54px;
    top: 80px;
    display: flex;
    align-items: center;
    gap: 26px;
  }
  .brand-dot {
    width: 72px;
    height: 72px;
    border-radius: 50%;
    background: var(--orange);
  }
  .brand-name {
    margin: 0;
    color: var(--orange);
    font-weight: 600;
    font-size: 27px;
    line-height: 32px;
    letter-spacing: 0.5px;
    text-transform: uppercase;
  }
  .tagline {
    position: absolute;
    left: 20px;
    right: 20px;
    top: 266px;
    margin: 0;
    color: var(--white);
    text-align: center;
    font-weight: 700;
    font-size: 39px;
    line-height: 47px;
    text-transform: uppercase;
    letter-spacing: 0.3px;
  }
  .benefits {
    position: absolute;
    left: 68px;
    top: 538px;
    margin: 0;
    padding: 0;
    list-style: none;
    color: var(--text);
    font-size: 18px;
    line-height: 27.5px;
  }
  .benefits li::before {
    content: "•";
    margin-right: 8px;
  }
  .client {
    position: absolute;
    transform: translate(-50%, -50%);
    display: flex;
    align-items: center;
    gap: 6px;
    white-space: nowrap;
    color: var(--navy);
    font-weight: 600;
    font-size: 21px;
  }
  .client-mark {
    width: 16px;
    height: 16px;
    background: var(--navy);
  }
  .client-mark.round { border-radius: 50%; }
  .partners-label {
    position: absolute;
    left: 136px;
    top: 890px;
    width: 168px;
    height: 30px;
    border-radius: 18px 4px 18px 4px;
    background: var(--navy);
    color: var(--white);
    font-size: 17px;
    line-height: 30px;
    text-align: center;
  }
  .partners-band {
    position: absolute;
    left: 0;
    right: 0;
    top: 930px;
    bottom: 0;
    background: var(--orange);
  }
  .partners-panel {
    position: absolute;
    left: 13px;
    right: 13px;
    top: 0;
    height: 118px;
    background: var(--white);
    border-radius: 0 0 24px 24px;
  }
  .partner {
    position: absolute;
    transform: translate(-50%, -50%);
    white-space: nowrap;
    color: var(--ink);
    font-weight: 600;
    font-size: 19px;
  }
</style>
</head>
<body>
  <main class="banner">
    <svg class="banner-shapes" width="440" height="1066" viewBox="0 0 440 1066" aria-hidden="true">
      <path class="navy-panel" d="M0,330 C0,262 48,220 125,220 L440,220 L440,600 L0,700 Z" fill="var(--navy)"/>
      <path class="orange-panel" d="M0,640 C0,545 55,500 150,500 L440,497 L440,560 C440,645 400,704 330,704 L0,704 Z" fill="var(--orange)" stroke="var(--white)" stroke-width="4"/>
      <rect x="0" y="704" width="440" height="20" fill="var(--white)"/>
    </svg>

    <header class="brand">
      <div class="brand-dot"></div>
      <p class="brand-name">Brightwave<br>Holdings</p>
    </header>

    <h1 class="tagline">Your Trusted<br>Partner in<br>Data-Driven<br>Decisions</h1>

    <ul class="benefits">
      <li>Unified data, analytics &amp; AI</li>
      <li>Trusted insights, faster outcomes</li>
      <li>Real-time intelligence at scale</li>
      <li>Enterprise-ready, secure solutions</li>
      <li>Clarity from data complexity</li>
    </ul>

    <section class="clients" aria-label="Trusted by">
      <div class="client" style="left:100px; top:767px;"><span class="client-mark"></span>Kestrel</div>
      <div class="client" style="left:226px; top:767px;"><span class="client-mark round"></span>Ambrook</div>
      <div class="client" style="left:346px; top:767px;">Norvane</div>
      <div class="client" style="left:130px; top:817px;">Tarnfield</div>
      <div class="client" style="left:300px; top:817px;"><span class="client-mark"></span>Harbour Lane</div>
    </section>

    <div class="partners-label">Partners with:</div>

    <section class="partners-band" aria-label="Partners">
      <div class="partners-panel">
        <div class="partner" style="left:123px; top:35px;">Clearpath</div>
        <div class="partner" style="left:289px; top:35px;">Tessera</div>
        <div class="partner" style="left:123px; top:76px;">Ledgerly</div>
        <div class="partner" style="left:289px; top:76px;">Quorix</div>
      </div>
    </section>
  </main>
</body>
</html>
```